BrightHarbor Flowchart Marketing Flyer

We are an MSP IT company. We have created a flowchart that we would like jazzed up to use in marketing new customers. The flowchart is a visual for prospective clients to see, in a simple way, what our process is. The flowchart should be 8.5"x11". We do not want the template of the flowchart altered (no boxes moved around) but would like something visually appealing and clean looking. Our office colors are lime green, royal blue, with accent colors of orange and purple. We would like the colors incorporated into the design. The design should be modern. This flyer is not going to be mass mailed. It will be handed to a prospective client in a face to face meeting.
Updates

I have uploaded our company logo to my brief in a couple of formats. One of the designers requested this. Great idea! I apologize for not providing it to begin with - it's my first time using this Website and the first time I have been assigned a project.

I was not able to view over the weekend as I did not have access to my work computer. Also need to review with the rest of management team on Thursday 6/28

Target Market(s)

Potential clients for an MSP IT company

Industry/Entity Type

It Company

Requirements
Must have
• The template itself we don't want changed. In other words we don't want the boxes moved around.
Nice to have
• Text, lines, shading and color of boxes can be changed. Not all colors mentioned in the brief need to be used. Would like it easy on the eye.

```html
<!DOCTYPE html>
<html lang="en">
<head>
<meta charset="utf-8">
<title>BrightHarbor Process</title>
<link href="https://fonts.googleapis.com/css2?family=Bebas+Neue&family=Cabin:wght@400;600;700&display=swap" rel="stylesheet">
<style>
  :root {
    --royal: #0f5cb0;
    --navy: #0b2d6b;
    --deep: #0d2a6b;
    --mid-blue: #2379bd;
    --light-blue: #3a93cc;
    --strategy-blue: #1b5fa8;
    --orange: #f58220;
    --heading-blue: #1d4f91;
    --body-grey: #555b63;
    --page-top: #f4f5f6;
    --page-bottom: #dcdfe2;
    --white: #ffffff;
  }
  * { box-sizing: border-box; margin: 0; padding: 0; }
  html, body { width: 1200px; height: 915px; overflow: hidden; background: #e9ebed; }
  .flyer {
    position: relative;
    width: 1200px;
    height: 915px;
    overflow: hidden;
    background: linear-gradient(160deg, var(--page-top) 0%, #eceef0 45%, var(--page-bottom) 100%);
    font-family: "Cabin", sans-serif;
  }
  .title-band { position: absolute; left: 0; top: 37px; width: 645px; height: 125px; }
  .title {
    position: absolute; left: 40px; top: 62px;
    font-family: "Bebas Neue", sans-serif; font-size: 70px; line-height: 1;
    color: var(--white); letter-spacing: 0.5px;
  }
  .rule {
    position: absolute; left: 0; top: 160px; width: 1200px; height: 10px;
    background: linear-gradient(90deg, var(--navy), var(--royal) 50%, var(--mid-blue));
    box-shadow: 0 4px 10px rgba(0,0,0,0.15);
  }
  .brand {
    position: absolute; left: 840px; top: 62px;
    display: flex; align-items: center; gap: 12px;
  }
  .brand-dot { width: 38px; height: 38px; border-radius: 50%; background: var(--royal); }
  .brand-name { font-family: "Cabin", sans-serif; font-weight: 700; font-size: 48px; color: var(--royal); }

  .cycle-heading {
    position: absolute; left: 799px; top: 210px;
    font-family: "Bebas Neue", sans-serif; font-size: 27px; color: var(--heading-blue);
  }

  .step { position: absolute; top: 363px; width: 224px; height: 182px; }
  .step svg { position: absolute; left: 0; top: 0; filter: drop-shadow(0 4px 5px rgba(0,0,0,0.18)); }
  .step-title {
    position: absolute; left: 0; top: 18px; width: 210px; text-align: center;
    font-family: "Bebas Neue", sans-serif; font-size: 25px; color: var(--white);
  }
  .step-list {
    position: absolute; left: 10px; top: 88px; list-style: none;
    font-size: 12.5px; line-height: 20px; color: var(--white);
  }
  .step-list li::before { content: "• "; }

  .cycle { position: absolute; left: 762px; top: 265px; }
  .cycle text { font-family: "Bebas Neue", sans-serif; fill: var(--white); }

  .priorities { position: absolute; left: 815px; top: 692px; list-style: none; }
  .priorities li {
    display: flex; align-items: center; gap: 8px;
    font-size: 16.5px; color: var(--body-grey); height: 28.5px;
  }
  .priorities svg { flex: none; }

  .contact-band { position: absolute; left: 0; top: 837px; width: 1200px; height: 78px; }
  .contact-call {
    position: absolute; left: 38px; top: 862px;
    font-family: "Bebas Neue", sans-serif; font-size: 30px; color: var(--white); letter-spacing: 0.6px;
  }
  .contact-item {
    position: absolute; top: 870px; display: flex; align-items: center; gap: 9px;
    font-size: 19px; color: var(--white); letter-spacing: 0.8px;
  }
</style>
</head>
<body>
<main class="flyer">

  <svg class="title-band" width="645" height="125" viewBox="0 0 645 125" aria-hidden="true">
    <defs>
      <linearGradient id="titleFill" x1="0" x2="1" y1="0" y2="0">
        <stop offset="0" stop-color="#0f5cb0"/>
        <stop offset="1" stop-color="#0b2d6b"/>
      </linearGradient>
    </defs>
    <path d="M0 0 H607 Q617 0 620 10 L645 125 H0 Z" fill="url(#titleFill)"/>
  </svg>
  <h1 class="title">BRIGHTHARBOR PROCESS</h1>
  <div class="rule"></div>

  <div class="brand">
    <span class="brand-dot"></span>
    <span class="brand-name">HarborTech</span>
  </div>

  <h2 class="cycle-heading">ONGOING STRATEGIC PLAN &amp; EXECUTION</h2>

  <section class="step" style="left:38px">
    <svg width="224" height="182" viewBox="0 0 224 182" aria-hidden="true">
      <path d="M0 54 L105 72 L210 54 V90 L222 104 L210 118 V170 Q210 182 198 182 H12 Q0 182 0 170 Z" fill="var(--royal)"/>
      <path d="M14 0 H196 Q210 0 210 14 V54 L105 74 L0 54 V14 Q0 0 14 0 Z" fill="var(--orange)"/>
    </svg>
    <h3 class="step-title">ASSESS ALIGNMENT</h3>
    <ul class="step-list">
      <li>Review Technology Philosophy</li>
      <li>Share Proprietary Method</li>
      <li>Assess Organizational Fit</li>
    </ul>
  </section>

  <section class="step" style="left:271px">
    <svg width="224" height="182" viewBox="0 0 224 182" aria-hidden="true">
      <path d="M0 54 L105 72 L210 54 V90 L222 104 L210 118 V170 Q210 182 198 182 H12 Q0 182 0 170 Z" fill="var(--royal)"/>
      <path d="M14 0 H196 Q210 0 210 14 V54 L105 74 L0 54 V14 Q0 0 14 0 Z" fill="var(--orange)"/>
    </svg>
    <h3 class="step-title">ON BOARDING</h3>
    <ul class="step-list">
      <li>Establish Expectations</li>
      <li>Service Provider Transition</li>
      <li>Cybersecurity Review</li>
      <li>Backup/Protection Strategy</li>
    </ul>
  </section>

  <section class="step" style="left:504px">
    <svg width="224" height="182" viewBox="0 0 224 182" aria-hidden="true">
      <path d="M0 54 L105 72 L210 54 V90 L222 104 L210 118 V170 Q210 182 198 182 H12 Q0 182 0 170 Z" fill="var(--royal)"/>
      <path d="M14 0 H196 Q210 0 210 14 V54 L105 74 L0 54 V14 Q0 0 14 0 Z" fill="var(--orange)"/>
    </svg>
    <h3 class="step-title">30 DAY EVALUATION</h3>
    <ul class="step-list">
      <li>Develop IT Playbook</li>
      <li>Major Risk Identification</li>
      <li>Observe &amp; Document Trends</li>
      <li>Standards Alignment Plan</li>
    </ul>
  </section>

  <svg class="cycle" width="416" height="404" viewBox="-8 -2 416 404" role="img" aria-label="Cycle of strategy, standards alignment, budget and risk assessment">
    <defs>
      <mask id="cycleCut">
        <rect x="-20" y="-20" width="440" height="440" fill="#fff"/>
        <line x1="0" y1="0" x2="400" y2="400" stroke="#000" stroke-width="16"/>
        <line x1="400" y1="0" x2="0" y2="400" stroke="#000" stroke-width="16"/>
        <circle cx="200" cy="200" r="70" fill="#000"/>
      </mask>
    </defs>
    <g mask="url(#cycleCut)">
      <path d="M200 200 L60 60 A198 198 0 0 1 340 60 Z" fill="var(--strategy-blue)"/>
      <path d="M200 200 L340 60 A198 198 0 0 1 340 340 Z" fill="var(--mid-blue)"/>
      <path d="M200 200 L340 340 A198 198 0 0 1 60 340 Z" fill="var(--light-blue)"/>
    </g>
    <g mask="url(#cycleCut)" transform="translate(-8 0)">
      <path d="M200 200 L60 340 A198 198 0 0 1 60 60 Z" fill="var(--orange)"/>
    </g>

    <!-- gears -->
    <g fill="none" stroke="#fff">
      <circle cx="190" cy="42" r="9" stroke-width="6" stroke-dasharray="3 2.6"/>
      <circle cx="190" cy="42" r="6" stroke-width="3"/>
      <circle cx="213" cy="32" r="8" stroke-width="1.6" stroke-dasharray="3 2"/>
      <circle cx="211" cy="57" r="7" stroke-width="5" stroke-dasharray="2.5 2.2"/>
      <circle cx="211" cy="57" r="4" stroke-width="2.5"/>
    </g>
    <text x="200" y="108" font-size="22" text-anchor="middle">STRATEGY</text>

    <!-- warning -->
    <path d="M76 142 L100 184 H52 Z" fill="#fff"/>
    <rect x="74" y="156" width="4" height="15" fill="var(--orange)"/>
    <rect x="74" y="174" width="4" height="4" fill="var(--orange)"/>
    <text x="76" y="211" font-size="21" text-anchor="middle">RISK</text>
    <text x="76" y="234" font-size="19" text-anchor="middle">ASSESSMENT</text>

    <!-- chart -->
    <g fill="#fff">
      <rect x="320" y="190" width="7" height="14"/>
      <rect x="331" y="182" width="7" height="22"/>
      <rect x="342" y="174" width="7" height="30"/>
      <rect x="353" y="166" width="7" height="38"/>
    </g>
    <path d="M318 182 L340 162 L348 170 L366 150" fill="none" stroke="#fff" stroke-width="3"/>
    <path d="M358 148 H368 V158" fill="none" stroke="#fff" stroke-width="3"/>
    <text x="337" y="241" font-size="21" text-anchor="middle">STANDARDS</text>
    <text x="337" y="264" font-size="21" text-anchor="middle">ALIGNMENT</text>

    <!-- budget -->
    <text x="201" y="308" font-size="21" text-anchor="middle">BUDGET</text>
    <g fill="none" stroke="#fff" stroke-width="2.5">
      <rect x="176" y="329" width="48" height="26"/>
      <rect x="182" y="323" width="48" height="26"/>
      <ellipse cx="200" cy="342" rx="7" ry="6"/>
    </g>
  </svg>

  <ul class="priorities">
    <li><svg width="15" height="15" viewBox="0 0 16 16" aria-hidden="true"><circle cx="8" cy="8" r="8" fill="var(--royal)"/><path d="M6.5 4.5 L10 8 L6.5 11.5" fill="none" stroke="#fff" stroke-width="2"/></svg>Develop &amp; Execute Annual Strategic Plan</li>
    <li><svg width="15" height="15" viewBox="0 0 16 16" aria-hidden="true"><circle cx="8" cy="8" r="8" fill="var(--royal)"/><path d="M6.5 4.5 L10 8 L6.5 11.5" fill="none" stroke="#fff" stroke-width="2"/></svg>Risk Assessment, Ranking, Mitigation</li>
    <li><svg width="15" height="15" viewBox="0 0 16 16" aria-hidden="true"><circle cx="8" cy="8" r="8" fill="var(--royal)"/><path d="M6.5 4.5 L10 8 L6.5 11.5" fill="none" stroke="#fff" stroke-width="2"/></svg>Prioritize Investments</li>
    <li><svg width="15" height="15" viewBox="0 0 16 16" aria-hidden="true"><circle cx="8" cy="8" r="8" fill="var(--royal)"/><path d="M6.5 4.5 L10 8 L6.5 11.5" fill="none" stroke="#fff" stroke-width="2"/></svg>Develop 5 Year Budget</li>
    <li><svg width="15" height="15" viewBox="0 0 16 16" aria-hidden="true"><circle cx="8" cy="8" r="8" fill="var(--royal)"/><path d="M6.5 4.5 L10 8 L6.5 11.5" fill="none" stroke="#fff" stroke-width="2"/></svg>HarborSolutionTM Standard Alignment</li>
  </ul>

  <svg class="contact-band" width="1200" height="78" viewBox="0 0 1200 78" aria-hidden="true">
    <defs>
      <linearGradient id="footFill" x1="0" x2="1" y1="0" y2="0">
        <stop offset="0" stop-color="#0b2d6b"/>
        <stop offset="1" stop-color="#0f3f8c"/>
      </linearGradient>
    </defs>
    <rect x="400" y="15" width="800" height="63" fill="url(#footFill)"/>
    <path d="M0 0 H458 Q466 0 469 8 L495 78 H0 Z" fill="var(--orange)"/>
  </svg>
  <p class="contact-call">CONTACT US TODAY FOR MORE INFORMATION</p>

  <p class="contact-item" style="left:510px">
    <svg width="16" height="16" viewBox="0 0 16 16" aria-hidden="true"><circle cx="8" cy="8" r="7.5" fill="#fff"/><rect x="3.5" y="5" width="9" height="6" fill="var(--deep)"/><path d="M3.5 5 L8 8.5 L12.5 5" fill="none" stroke="#fff" stroke-width="1"/></svg>
    info@harbortech.com
  </p>
  <p class="contact-item" style="left:737px">
    <svg width="18" height="18" viewBox="0 0 18 18" aria-hidden="true"><circle cx="9" cy="9" r="8" fill="none" stroke="#fff" stroke-width="1.5"/><path d="M6 4.5 L7.8 7 L6.8 8.2 Q7.8 10.4 9.8 11.2 L11 10.2 L13.5 12 L12.5 13.5 Q8 14 4.5 6 Z" fill="#fff"/></svg>
    &nbsp;(555)014-2400
  </p>
  <p class="contact-item" style="left:908px">
    <svg width="18" height="18" viewBox="0 0 18 18" aria-hidden="true"><g fill="none" stroke="#fff" stroke-width="1.3"><circle cx="9" cy="9" r="7.5"/><ellipse cx="9" cy="9" rx="3.5" ry="7.5"/><path d="M1.5 9 H16.5 M3 5 H15 M3 13 H15"/></g></svg>
    www.harbortech.com
  </p>

</main>
</body>
</html>
```